Camp Thornbury Retreat Brochure

We are looking for someone to design a brochure/flyer that we can use to promote renting our camp facility. We don't have a specific size in mind, we are open to different options.

The link below has pictures that can be used (don't expect you to use all of them). It also has a PDF of the information that will need to be included in the brochure.

https://files.quillbox.example/folders/7KpR2-TmXa9LwQzB4nYcHd8-vUe3Fs6?usp=sharing

We are a Christian camp and retreat facility. You might want to check out our website to get a feel for what we do.

This brochure will be used to help us increase our rental business. Usually given to an organizational leader who is planning a retreat.

Target Market(s)

Church groups, community groups

Industry/Entity Type

Rental

Requirements
Must have
• Pictures
Information that was included
Website
Contact Information
Nice to have
• Logo
Should not have
• Cross
Clip art

```html
<!DOCTYPE html>
<html lang="en">
<head>
<meta charset="utf-8">
<title>Camp Thornbury Retreat Brochure – Facilities &amp; Activities</title>
<link href="https://fonts.googleapis.com/css2?family=Oswald:wght@500&family=Montserrat:wght@500;600&display=swap" rel="stylesheet">
<style>
  :root{
    --backdrop:#5b5b5b;
    --paper:#eef0f3;
    --heading-green:#2f6b4f;
    --text-dark:#2b2b2b;
    --accent-orange:#e09a55;
    --band-orange:#d8935a;
    --band-olive:#979a6c;
    --band-green:#6a9d7c;
    --field-tan:#c8955f;
    --field-olive:#8e9a74;
    --field-green:#5f9479;
    --photo-wood:#8a5a34;
    --photo-forest:#6f8c5a;
  }
  *{box-sizing:border-box;margin:0;padding:0}
  html,body{width:1200px;height:789px;overflow:hidden}
  body{background:var(--backdrop);position:relative;font-family:"Montserrat",Arial,sans-serif}

  .spread{position:absolute;left:80px;top:24px;width:1040px;height:740px;display:flex;box-shadow:0 12px 30px rgba(0,0,0,.35)}
  .page{position:relative;width:520px;height:740px;background:var(--paper);overflow:hidden}
  .page-left{box-shadow:inset -18px 0 24px -18px rgba(0,0,0,.18)}
  .page-right{box-shadow:inset 18px 0 24px -18px rgba(0,0,0,.18)}
  .page-shapes{position:absolute;inset:0;width:100%;height:100%}

  .section-title{position:absolute;font-family:"Oswald",Arial Narrow,sans-serif;font-weight:500;font-size:30px;letter-spacing:.5px;color:var(--heading-green)}
  .dotted-rule{position:absolute;height:0;border-top:2px dotted var(--accent-orange)}

  .check-list{position:absolute;list-style:none}
  .check-list li{position:relative;padding-left:24px;font-size:14.5px;line-height:21px;font-weight:500;color:var(--text-dark);white-space:nowrap}
  .check-list li::before{content:"";position:absolute;left:0;top:4px;width:13px;height:13px;border:1.5px solid var(--accent-orange);border-radius:50%}
  .check-list li::after{content:"";position:absolute;left:4px;top:7px;width:5px;height:3px;border-left:1.5px solid var(--accent-orange);border-bottom:1.5px solid var(--accent-orange);transform:rotate(-45deg)}

  .photo{position:absolute;box-shadow:0 3px 10px rgba(0,0,0,.35);border:3px solid #fff}
  .photo::after{content:"";position:absolute;inset:6px;border:1px solid rgba(255,255,255,.85)}
  .photo-bunks{background:linear-gradient(135deg,#d8cbb4,var(--photo-wood) 60%,#e6d9a0)}
  .photo-hall{background:linear-gradient(160deg,#5a3820,#9a6b40 45%,#3c2a22)}
  .photo-cabins{background:linear-gradient(180deg,#b9cfa8,var(--photo-forest) 55%,#9c4a34 80%,#cfcfc6)}
  .photo-pavilion{background:linear-gradient(180deg,#c4d6b2,#6f8c5a 55%,#bdb7ad)}
  .photo-lodge{background:linear-gradient(180deg,#c9d9b7,#7b9563 50%,#b79a7c 75%,#d4d2c8)}
  .tree-backdrop{position:absolute;left:140px;top:60px;width:380px;height:520px;background:radial-gradient(ellipse at 60% 40%,rgba(150,165,150,.35),rgba(238,240,243,0) 70%)}
</style>
</head>
<body>
<main class="spread">

  <section class="page page-left" aria-label="Facilities">
    <svg class="page-shapes" viewBox="0 0 520 740" preserveAspectRatio="none" aria-hidden="true">
      <defs>
        <linearGradient id="bandLeft" x1="0" x2="1"><stop offset="0" stop-color="var(--band-orange)"/><stop offset="1" stop-color="var(--band-olive)"/></linearGradient>
        <linearGradient id="fieldLeft" x1="0" x2="1"><stop offset="0" stop-color="var(--field-tan)"/><stop offset="1" stop-color="var(--field-olive)"/></linearGradient>
      </defs>
      <path fill="url(#bandLeft)" d="M0 0H520V30L494 54L468 30L442 54L416 30L390 54L364 30L338 54L312 30L286 54L260 30L234 54L208 30L182 54L156 30L130 54L104 30L78 54L52 30L26 54L0 30Z"/>
      <path fill="url(#fieldLeft)" d="M0 372L26 348L52 372L78 348L104 372L130 348L156 372L182 348L208 372L234 348L260 372L286 348L312 372L338 348L364 372L390 348L416 372L442 348L468 372L494 348L520 372V740H0Z"/>
    </svg>
    <h2 class="section-title" style="left:44px;top:74px">FACILITIES:</h2>
    <div class="dotted-rule" style="left:44px;top:124px;width:430px"></div>
    <ul class="check-list" style="left:48px;top:140px">
      <li>26 Cabins (sleep 10-12)</li>
      <li>Commercial Kitchen</li>
      <li>Dining Hall (seats 150)</li>
      <li>3 Pavilions</li>
      <li>Covered Gym (with lights)</li>
      <li>Pool</li>
      <li>Recreational Lake</li>
      <li>Sand Volleyball Pit (with lights)</li>
      <li>Softball Field (with lights)</li>
      <li>Campfire Pit</li>
    </ul>
    <div class="photo photo-bunks" role="img" aria-label="Cabin interior with wooden bunk beds" style="left:34px;top:402px;width:200px;height:190px"></div>
    <div class="photo photo-hall" role="img" aria-label="Dining hall with timber roof and chandeliers" style="left:206px;top:430px;width:290px;height:250px"></div>
  </section>

  <section class="page page-right" aria-label="Activities">
    <div class="tree-backdrop" role="img" aria-label="Faint misty tree canopy"></div>
    <svg class="page-shapes" viewBox="0 0 520 740" preserveAspectRatio="none" aria-hidden="true">
      <path fill="var(--band-green)" d="M0 0H520V30L494 54L468 30L442 54L416 30L390 54L364 30L338 54L312 30L286 54L260 30L234 54L208 30L182 54L156 30L130 54L104 30L78 54L52 30L26 54L0 30Z"/>
      <path fill="var(--field-green)" d="M0 452L26 428L52 452L78 428L104 452L130 428L156 452L182 428L208 452L234 428L260 452L286 428L312 452L338 428L364 452L390 428L416 452L442 428L468 452L494 428L520 452V740H0Z"/>
    </svg>
    <h2 class="section-title" style="left:44px;top:74px">ACTIVITIES:</h2>
    <div class="dotted-rule" style="left:44px;top:124px;width:430px"></div>
    <ul class="check-list" style="left:48px;top:140px">
      <li>Horseback Riding</li>
      <li>Low Ropes Course</li>
      <li>Hatchet Throwing</li>
      <li>Archery Tag</li>
      <li>Fishing</li>
      <li>Volleyball</li>
      <li>Softball</li>
    </ul>
    <ul class="check-list" style="left:250px;top:182px">
      <li>Gaga Ball</li>
      <li>Grid Square Volley</li>
      <li>Basketball</li>
      <li>Swimming (seasonal)</li>
      <li>Hiking</li>
      <li>Soccer</li>
    </ul>
    <div class="photo photo-cabins" role="img" aria-label="Red cabins among tall trees" style="left:30px;top:470px;width:300px;height:150px"></div>
    <div class="photo photo-pavilion" role="img" aria-label="Open pavilion under shade trees" style="left:24px;top:600px;width:150px;height:115px"></div>
    <div class="photo photo-lodge" role="img" aria-label="Lodge building beside a gravel path" style="left:182px;top:606px;width:160px;height:115px"></div>
  </section>

</main>
</body>
</html>
```